WRM Marketing Postcard

Design a 2 Sided marketing postcard for our Real estate management caompany. Looking for a professional yet fresh look that will be printed on a 6"x9" glossy flier

Contact information is www.wexleymanagement.com wexleymanagement@inboxvane.com and 312-555-0187

WE are targeting small condo and town home properties to take on their administrative responsibilities of management

```html
<!DOCTYPE html>
<html lang="en">
<head>
<meta charset="utf-8">
<title>WRM Marketing Postcard</title>
<link rel="stylesheet" href="https://fonts.googleapis.com/css2?family=Lato:wght@400;700;900&display=swap">
<style>
:root{
  --page:#e4e5e7;
  --paper:#ffffff;
  --red:#d0141c;
  --navy:#1c3563;
  --navy-deep:#14284d;
  --blue:#3f6eab;
  --band:#c4dcfa;
  --ink:#1d2c4a;
  --photo-a:#aeb9c8;
  --photo-b:#7e8ea6;
  --line:#b9bcc2;
}
*{box-sizing:border-box;margin:0;padding:0}
html,body{width:1200px;height:900px;overflow:hidden}
body{background:var(--page);font-family:"Lato",sans-serif;position:relative}
.card{position:absolute;width:630px;height:420px;background:var(--paper);overflow:hidden;box-shadow:0 6px 18px rgba(0,0,0,.18)}
.card svg.decor{position:absolute;inset:0;width:100%;height:100%}
.front{left:40px;top:30px}
.back{left:530px;top:450px}

/* front */
.front .title{position:absolute;left:24px;top:22px;color:var(--red);font-weight:900;font-size:22px;line-height:1.05;white-space:nowrap}
.front .tagline{position:absolute;left:24px;top:74px;width:300px;color:var(--navy);font-weight:700;font-size:12px;line-height:1.2}
.section{position:absolute;left:24px;width:285px;color:var(--ink)}
.section h2{font-size:13px;font-weight:700;color:var(--navy);margin-bottom:2px}
.section p{font-size:7.5px;line-height:1.3}
.who{top:116px}
.why{top:175px}
.what{top:256px}
.tasks{list-style:none;font-size:7.5px;line-height:1.28}
.tasks li{position:relative;padding-left:10px}
.tasks li::before{content:"";position:absolute;left:1px;top:2px;width:3px;height:5px;border:solid var(--red);border-width:0 1.5px 1.5px 0;transform:rotate(40deg)}
.contact{position:absolute;color:#fff;font-size:8.5px;display:flex;align-items:center;gap:5px;white-space:nowrap}
.contact svg{width:9px;height:9px}
.c-web{left:40px;top:404px}
.c-mail{left:240px;top:404px}
.c-phone{left:510px;top:370px;font-weight:700;font-size:10px}

/* back */
.back .title{position:absolute;left:28px;top:32px;color:#fff;font-weight:900;font-size:25px;line-height:1.05;white-space:nowrap}
.benefits{position:absolute;left:30px;top:108px;width:305px;list-style:none;color:#fff;font-weight:700;font-size:11px;line-height:1.22}
.benefits li{position:relative;padding-left:18px;margin-bottom:7px}
.benefits li svg{position:absolute;left:0;top:3px;width:11px;height:10px}
.call{position:absolute;left:60px;top:345px;color:#fff;font-weight:900;text-align:center}
.call .label{font-size:15px}
.call .number{font-size:30px;letter-spacing:.5px}
.stamp{position:absolute;left:515px;top:24px;width:78px;height:86px;border:1.5px solid var(--line)}
</style>
</head>
<body>

<section class="card front" aria-label="Postcard front">
  <svg class="decor" viewBox="0 0 630 420">
    <defs>
      <linearGradient id="photoTone" x1="0" y1="0" x2="1" y2="1">
        <stop offset="0" stop-color="var(--photo-a)"/>
        <stop offset="1" stop-color="var(--photo-b)"/>
      </linearGradient>
    </defs>
    <polygon points="0,106 345,106 330,150 318,248 0,248" fill="var(--band)"/>
    <polygon role="img" aria-label="Photo of a model house and house keys resting on building plans" points="420,0 630,0 630,330 420,330 350,210" fill="url(#photoTone)"/>
    <polyline points="413,0 343,210 413,330" fill="none" stroke="var(--navy)" stroke-width="4"/>
    <polyline points="404,0 334,210 404,330" fill="none" stroke="var(--navy)" stroke-width="2"/>
    <polygon points="0,396 310,396 370,330 630,330 630,420 0,420" fill="var(--navy)"/>
  </svg>

  <h1 class="title">WEXLEY PROPERTY<br>MANAGEMENT LLC (“WRM”)</h1>
  <p class="tagline">Improve compliance, reporting, and communication amongst all owners and board members</p>

  <div class="section who">
    <h2>Who we are</h2>
    <p>A professional services organization with a focus on small (3-10 unit) residential buildings over 30 years of combined experience in real estate and property management. Professional, courteous, timely service that is technologically driven</p>
  </div>
  <div class="section why">
    <h2>Why use WRM?</h2>
    <p>Owners are rarely suited to manage associations and the burden often falls unfairly on one or two individuals to do all the work low monthly fees tailored to your needs. The association’s board of directors maintains control of all decision making.</p>
  </div>
  <div class="section what">
    <h2>What we do</h2>
    <ul class="tasks">
      <li>Remove the administrative burden of managing small residential buildings</li>
      <li>Utilize economies of scale to reduce expenses for all owners across a wide variety of service providers</li>
      <li>Collect all assessments and pay all bills</li>
      <li>Provide monthly accounting reconciliation and reporting</li>
      <li>Provide access to WRM’s client portal with a central repository of all association materials (bylaws, financials, meeting minutes, communications, etc)</li>
      <li>Issue 1099s to all contractors as required by law</li>
      <li>Prepare year-end financial statements</li>
      <li>Lender and legal HOA documents for mortgage companies and sales</li>
    </ul>
  </div>

  <div class="contact c-web">
    <svg viewBox="0 0 10 10"><circle cx="5" cy="5" r="4" fill="none" stroke="#fff" stroke-width="1"/><path d="M1 5h8M5 1c-2 2.5-2 5.5 0 8M5 1c2 2.5 2 5.5 0 8" fill="none" stroke="#fff" stroke-width=".8"/></svg>
    www.wexleymanagement.com
  </div>
  <div class="contact c-mail">
    <svg viewBox="0 0 10 10"><rect x="1" y="2" width="8" height="6" fill="none" stroke="#fff" stroke-width="1"/><path d="M1 2l4 3.5L9 2" fill="none" stroke="#fff" stroke-width="1"/></svg>
    wexleymanagement@inboxvane.com
  </div>
  <div class="contact c-phone">
    <svg viewBox="0 0 10 10"><rect x="0" y="0" width="10" height="10" rx="2" fill="#fff"/><path d="M3 2.5l1.2 1.5-.7.8c.5 1 1.2 1.7 2 2.1l.8-.7 1.5 1.2-.8 1c-2.3-.4-4.2-2.4-4.6-4.8z" fill="var(--navy)"/></svg>
    312-555-0187
  </div>
</section>

<section class="card back" aria-label="Postcard back">
  <svg class="decor" viewBox="0 0 630 420">
    <polygon points="0,0 405,0 340,420 0,420" fill="var(--blue)"/>
    <polygon points="0,352 352,322 338,420 0,420" fill="var(--navy-deep)"/>
    <g stroke="var(--line)" stroke-width="1">
      <line x1="390" y1="250" x2="605" y2="250"/>
      <line x1="388" y1="276" x2="605" y2="276"/>
      <line x1="386" y1="302" x2="605" y2="302"/>
      <line x1="384" y1="328" x2="605" y2="328"/>
    </g>
  </svg>
  <div class="stamp" aria-label="Stamp area"></div>

  <h1 class="title">WEXLEY PROPERTY<br>MANAGEMENT LLC (“WRM”)</h1>
  <ul class="benefits">
    <li><svg viewBox="0 0 11 10"><path d="M1 5.5l3 3L10 1" fill="none" stroke="#fff" stroke-width="2"/></svg>Cost effective property management solution for 3-10 unit buildings</li>
    <li><svg viewBox="0 0 11 10"><path d="M1 5.5l3 3L10 1" fill="none" stroke="#fff" stroke-width="2"/></svg>Prices starting as low as $100/month</li>
    <li><svg viewBox="0 0 11 10"><path d="M1 5.5l3 3L10 1" fill="none" stroke="#fff" stroke-width="2"/></svg>Utilize our economies of scale to reduce costs across existing services (trash, insurance, maintenance, etc)</li>
    <li><svg viewBox="0 0 11 10"><path d="M1 5.5l3 3L10 1" fill="none" stroke="#fff" stroke-width="2"/></svg>Eliminate the unfair burden placed on a few owners to do all the work while others free-ride</li>
    <li><svg viewBox="0 0 11 10"><path d="M1 5.5l3 3L10 1" fill="none" stroke="#fff" stroke-width="2"/></svg>Improve communication amongst all owners and board members</li>
    <li><svg viewBox="0 0 11 10"><path d="M1 5.5l3 3L10 1" fill="none" stroke="#fff" stroke-width="2"/></svg>The association’s board of directors maintain all decision-making power</li>
    <li><svg viewBox="0 0 11 10"><path d="M1 5.5l3 3L10 1" fill="none" stroke="#fff" stroke-width="2"/></svg>Utilize our vetted service providers for prompt job completion and fair pricing</li>
  </ul>
  <div class="call">
    <div class="label">Call us</div>
    <div class="number">312-555-0187</div>
  </div>
</section>

</body>
</html>
```